" Oferecemos diagnósticos para definir os pontos de oportunidade de melhoria, depois elaboramos um projeto que começa pela criação de indicadores (que mostram o desempenho mês a mês) e ajudamos o cliente e elaborar um plano de ação para melhorar os indicadores, assim garantimos que os resultados melhorem de forma consistente e real. Garantimos o resultado se o cliente se envolver e executar as ações. Pois nosso negócio é entregar resultados. "

```html
<!DOCTYPE html>
<html lang="pt">
<head>
<meta charset="utf-8">
<title>Veltra — Pasta institucional</title>
<link href="https://fonts.googleapis.com/css2?family=Montserrat:wght@400;600&display=swap" rel="stylesheet">
<style>
  :root {
    --backdrop: #e9eaec;
    --paper: #ffffff;
    --paper-shade: #f1f2f4;
    --fold-line: #dfe1e5;
    --navy: #0f1c2e;
    --navy-deep: #08111d;
    --accent: #2bb3e6;
    --ink-light: #ffffff;
    --ink-muted: #9fb3c8;
  }
  * { margin: 0; padding: 0; box-sizing: border-box; }
  html, body {
    width: 1200px;
    height: 1200px;
    overflow: hidden;
    background: var(--backdrop);
    font-family: "Montserrat", sans-serif;
  }
  .folder {
    position: absolute;
    left: 110px;
    top: 140px;
    width: 980px;
    height: 920px;
    display: flex;
    box-shadow: 0 18px 40px rgba(0,0,0,0.12);
  }
  .folder-cover-edge {
    position: absolute;
    left: 110px;
    top: 1060px;
    width: 490px;
    height: 8px;
    background: var(--accent);
  }
  .panel {
    position: relative;
    width: 490px;
    height: 100%;
    background: var(--paper);
  }
  .panel-left {
    background: linear-gradient(90deg, var(--paper) 0%, var(--paper) 85%, var(--paper-shade) 100%);
    border-right: 1px solid var(--fold-line);
  }
  .panel-right {
    background: linear-gradient(90deg, var(--paper-shade) 0%, var(--paper) 12%, var(--paper) 100%);
  }
  .pocket {
    position: absolute;
    left: 0;
    right: 0;
    bottom: 0;
    height: 300px;
    background: linear-gradient(135deg, var(--navy) 0%, var(--navy-deep) 100%);
    border-top: 3px solid var(--accent);
  }
  .card-slit {
    position: absolute;
    left: 0;
    top: -3px;
    width: 60px;
    height: 40px;
  }
  .brand {
    position: absolute;
    left: 70px;
    top: 100px;
    display: flex;
    flex-direction: column;
    gap: 10px;
  }
  .brand-row {
    display: flex;
    align-items: center;
    gap: 14px;
  }
  .brand-dot {
    width: 18px;
    height: 18px;
    border-radius: 50%;
    background: var(--accent);
  }
  .brand-name {
    color: var(--ink-light);
    font-weight: 600;
    font-size: 64px;
    letter-spacing: 4px;
    line-height: 1;
  }
  .brand-tagline {
    color: var(--ink-muted);
    font-weight: 400;
    font-size: 13px;
    letter-spacing: 3px;
    text-transform: uppercase;
    padding-left: 34px;
  }
</style>
</head>
<body>
  <div class="folder">
    <section class="panel panel-left"></section>
    <section class="panel panel-right">
      <div class="pocket">
        <svg class="card-slit" viewBox="0 0 60 40" aria-hidden="true">
          <polygon points="0,0 60,0 0,40" fill="#ffffff"/>
        </svg>
        <div class="brand">
          <div class="brand-row">
            <span class="brand-dot"></span>
            <span class="brand-name">VELTRA</span>
          </div>
          <span class="brand-tagline">consultoria para resultados</span>
        </div>
      </div>
    </section>
  </div>
  <div class="folder-cover-edge"></div>
</body>
</html>
```